Short term accommodation - Guest feedback flyer

We provide short term fully self contained accommodation for couples,families and friends who require accommodation close to Brisbane City. We have 3 properties - http://www.nestora.com.au/accommodation/qld/brisbane/fernwick. Our properties are advertised on a on a number of online booking sites - such as wander ledger, roam nest, nestora etc. Our accommodation is fully self contained, a roam nest from home! Our accommodation is affordable and located near or on transport routes so our guests can travel to all tourist attractions with ease. We provide a personal, professional and family friendly experience and we would like to capture our guests comments on their stay with the view to then posting their comments online so other guests can read about their experiences. Most guests don't have the time to leave their comments online once they check out. Id like a flyer to give to them before they check out so they have time to provide their feedback before they leave, I'll then take their feedback and upload it for them. A lot of travellers like to read online reviews before they book and I'd like the flyer to make it easy for guests to leave their feedback and I'll take it and post it for them. I hope by posting more comments on our webpages that our bookings will increase. Im happy for your to use any of the images/photos that are used on our nestora pages…….ive added the link about. Id like one generic flyer that I can use for all 3 properties please.

Thanks.

```html
<!DOCTYPE html>
<html lang="en">
<head>
<meta charset="utf-8">
<title>Guest Feedback Card</title>
<link href="https://fonts.googleapis.com/css2?family=Tinos:ital,wght@0,400;0,700;1,400&family=Pinyon+Script&display=swap" rel="stylesheet">
<style>
  :root {
    --page: #ffffff;
    --sage: #b9bd95;
    --sage-light: #c8cfa3;
    --cream: #faf4bd;
    --cream-edge: #e9e2a0;
    --red: #c0383a;
    --ink: #1a1a1a;
    --ink-soft: #333333;
    --rule: #7a7a7a;
  }
  * { margin: 0; padding: 0; box-sizing: border-box; }
  html, body { width: 1200px; height: 1000px; overflow: hidden; background: var(--page); }
  body { position: relative; font-family: "Tinos", "Times New Roman", serif; color: var(--ink); }
  h1, h2 { font-weight: 400; }

  /* Front of card */
  .card-front {
    position: absolute; left: 323px; top: 36px; width: 551px; height: 431px;
    background: var(--sage); overflow: hidden;
  }
  .front-illustration {
    position: absolute; left: 0; top: 0; width: 100%; height: 162px;
    background: linear-gradient(180deg, #cdd3a8 0%, var(--sage-light) 60%, #c3c99c 100%);
  }
  .lace-band {
    position: absolute; left: 0; top: 162px; width: 100%; height: 22px;
    background: var(--cream);
    border-top: 2px solid var(--cream-edge);
  }
  .thank-you {
    position: absolute; left: 0; right: 0; top: 200px; text-align: center;
    font-family: "Pinyon Script", cursive; font-weight: 400; font-size: 80px; line-height: 1;
    color: var(--red);
  }
  .stay-line {
    position: absolute; left: 0; right: 0; top: 308px; text-align: center;
    font-size: 16.5px; letter-spacing: 0.6px;
  }
  .feedback-head {
    position: absolute; left: 0; right: 0; top: 347px; text-align: center;
    font-size: 10.5px; letter-spacing: 0.5px;
  }
  .feedback-note {
    position: absolute; left: 0; right: 0; top: 364px; text-align: center;
    font-size: 10.5px; font-style: italic;
  }
  .property-list {
    position: absolute; left: 0; right: 0; top: 401px; text-align: center;
    font-size: 9.5px; font-weight: 700; letter-spacing: 2px;
  }
  .property-list .divider { color: #a06a55; font-weight: 400; margin: 0 6px; }

  /* Back of card */
  .card-back {
    position: absolute; left: 326px; top: 542px; width: 551px; height: 430px;
    background: var(--page);
  }
  .side-band { position: absolute; top: 0; height: 100%; width: 74px; }
  .side-band .sage-strip { position: absolute; top: 0; height: 100%; width: 50px; background: var(--sage); }
  .side-band .lace-strip { position: absolute; top: 0; height: 100%; width: 24px; background: var(--cream); }
  .side-band--left { left: 0; }
  .side-band--left .sage-strip { left: 0; }
  .side-band--left .lace-strip { left: 50px; border-left: 2px solid var(--cream-edge); }
  .side-band--right { right: 0; }
  .side-band--right .sage-strip { right: 0; }
  .side-band--right .lace-strip { right: 50px; border-right: 2px solid var(--cream-edge); }

  .back-content { position: absolute; left: 74px; width: 403px; top: 0; height: 100%; text-align: center; color: var(--ink-soft); }
  .form-title { position: absolute; left: 0; right: 0; top: 28px; font-size: 13.5px; letter-spacing: 0.3px; color: var(--ink); }
  .property-options {
    position: absolute; left: 0; right: 0; top: 59px;
    display: flex; justify-content: center; gap: 20px; font-size: 10.5px;
  }
  .option { display: flex; align-items: center; gap: 6px; }
  .checkbox { width: 11px; height: 11px; border: 1px solid #777; display: inline-block; background: #fff; }
  .prompt { position: absolute; left: 0; right: 0; top: 123px; font-size: 10.5px; }
  .write-line {
    position: absolute; left: 28px; width: 348px; height: 0;
    border-top: 1.5px dotted var(--rule);
  }
  .permission { position: absolute; left: 0; right: 0; top: 322px; font-size: 10.5px; line-height: 15px; }
  .permission .checkbox { vertical-align: -2px; margin-left: 4px; }
  .sign-off { position: absolute; left: 0; right: 0; top: 369px; font-size: 10.5px; }
  .signature {
    position: absolute; left: 0; right: 0; top: 383px;
    font-family: "Pinyon Script", cursive; font-size: 21px; color: var(--red);
  }
</style>
</head>
<body>

<section class="card-front">
  <div class="front-illustration" role="img" aria-label="Illustration of three whimsical cottages with red roofs under falling snow"></div>
  <div class="lace-band" role="img" aria-label="Cream lace trim band"></div>
  <h1 class="thank-you">Thank You</h1>
  <p class="stay-line">FOR CHOOSING TO STAY WITH US</p>
  <p class="feedback-head">WE’D LOVE TO HEAR YOUR FEEDBACK!</p>
  <p class="feedback-note">Please take a few moments to complete the reverse of this card.</p>
  <p class="property-list">ASHCOMBE HOUSE<span class="divider">|</span>LINDEN TERRACE<span class="divider">|</span>FERNWICK APARTMENT</p>
</section>

<section class="card-back">
  <div class="side-band side-band--left" role="img" aria-label="Sage band with cream lace trim">
    <div class="sage-strip"></div><div class="lace-strip"></div>
  </div>
  <div class="side-band side-band--right" role="img" aria-label="Sage band with cream lace trim">
    <div class="sage-strip"></div><div class="lace-strip"></div>
  </div>

  <div class="back-content">
    <h2 class="form-title">NAME OF PROPERTY</h2>
    <div class="property-options">
      <span class="option"><span class="checkbox"></span>Ashcombe House</span>
      <span class="option"><span class="checkbox"></span>Linden Terrace</span>
      <span class="option"><span class="checkbox"></span>Fernwick Apartment</span>
    </div>
    <p class="prompt">Please tell us in a few words about your experience</p>
    <div class="write-line" style="top:162px"></div>
    <div class="write-line" style="top:193px"></div>
    <div class="write-line" style="top:225px"></div>
    <div class="write-line" style="top:255px"></div>
    <div class="write-line" style="top:285px"></div>
    <p class="permission">We’d love to post your comments online so that other guests can read them too.<br>Please tick the box to let us know that’s OK<span class="checkbox"></span></p>
    <p class="sign-off">Safe travels,</p>
    <p class="signature">Tessa Marlowe</p>
  </div>
</section>

</body>
</html>
```